Corvell Advisory

Business Development Consulting Firm

Target Market(s)

Federal Government, 8(a) companies, Small Businesses

Industry/Entity Type

Private Sector, US Government

Contact Information for Business Card

8(a) Program Capture, Business Development, Industry Trends & Analysis, Strategic Teaming, Cyber Solutions

Colors

Designer to choose colors to be used in the design.

```html
<!DOCTYPE html>
<html lang="en">
<head>
<meta charset="UTF-8">
<title>Corvell Advisory — Business Cards</title>
<link rel="stylesheet" href="https://fonts.googleapis.com/css2?family=Montserrat:wght@500;600&family=Roboto:wght@400&display=swap">
<style>
  :root {
    --backdrop: #d3d6d7;
    --paper: #efefed;
    --brand-blue: #0c3fa6;
    --ink: #333536;
    --rule: #4a4c4d;
    --edge: #0b2f9a;
  }
  * { margin: 0; padding: 0; box-sizing: border-box; }
  html, body { width: 1200px; height: 1050px; overflow: hidden; }
  body {
    background: var(--backdrop);
    font-family: "Roboto", Arial, sans-serif;
    color: var(--ink);
    position: relative;
  }
  .card {
    position: absolute;
    left: 250px;
    width: 700px;
    height: 400px;
    background: var(--paper);
    border-bottom: 5px solid var(--edge);
    box-shadow: 0 14px 30px rgba(0,0,0,0.18);
  }
  .card--front { top: 95px; }
  .card--back { top: 555px; }

  .wordmark {
    display: flex;
    align-items: center;
    gap: 16px;
    color: var(--brand-blue);
    font-family: "Montserrat", Arial, sans-serif;
    font-weight: 500;
    text-transform: uppercase;
  }
  .wordmark__dot {
    border-radius: 50%;
    background: var(--brand-blue);
    flex: none;
  }
  .card--front .wordmark {
    position: absolute;
    left: 0; right: 0; top: 140px;
    justify-content: center;
    font-size: 44px;
    letter-spacing: 4px;
  }
  .card--front .wordmark__dot { width: 40px; height: 40px; }

  .services {
    position: absolute;
    left: 0; right: 0; bottom: 40px;
    text-align: center;
    font-size: 13px;
    color: var(--ink);
  }
  .services__sep {
    display: inline-block;
    width: 6px; height: 6px;
    border-radius: 50%;
    background: var(--brand-blue);
    margin: 0 8px;
    vertical-align: middle;
  }

  .person {
    position: absolute;
    left: 48px; top: 52px;
  }
  .person__name {
    font-family: "Montserrat", Arial, sans-serif;
    font-weight: 600;
    font-size: 21px;
    letter-spacing: 1px;
    color: var(--brand-blue);
    text-transform: uppercase;
  }
  .person__title { font-size: 18px; margin-top: 4px; }
  .contact-list {
    list-style: none;
    margin-top: 16px;
    font-size: 18px;
  }
  .contact-list li {
    display: flex;
    align-items: center;
    gap: 10px;
    margin-bottom: 8px;
  }
  .contact-list svg { width: 18px; height: 18px; flex: none; }

  .card--back .wordmark {
    position: absolute;
    right: 44px; top: 60px;
    font-size: 25px;
    letter-spacing: 2px;
    gap: 10px;
  }
  .card--back .wordmark__dot { width: 24px; height: 24px; }
  .divider {
    position: absolute;
    left: 330px; right: 44px; top: 235px;
    height: 1px;
    background: var(--rule);
  }
  .address {
    position: absolute;
    right: 44px; top: 262px;
    text-align: right;
    font-size: 19px;
    line-height: 1.4;
    font-style: normal;
  }
</style>
</head>
<body>

<section class="card card--front">
  <div class="wordmark"><span class="wordmark__dot"></span>Corvell Advisory</div>
  <p class="services">8(a) Program Capture<span class="services__sep"></span>Industry Trends &amp; Analysis<span class="services__sep"></span>Strategic Teaming</p>
</section>

<section class="card card--back">
  <div class="person">
    <h1 class="person__name">Marcus J. Pellerin</h1>
    <p class="person__title">Founder &amp; CEO</p>
    <ul class="contact-list">
      <li>
        <svg viewBox="0 0 24 24" aria-hidden="true"><path fill="#0c3fa6" d="M6.6 10.8a15.1 15.1 0 0 0 6.6 6.6l2.2-2.2a1 1 0 0 1 1-.25 11.4 11.4 0 0 0 3.6.57 1 1 0 0 1 1 1V20a1 1 0 0 1-1 1A17 17 0 0 1 3 4a1 1 0 0 1 1-1h3.5a1 1 0 0 1 1 1c0 1.25.2 2.45.57 3.57a1 1 0 0 1-.25 1z"/></svg>
        (555) 014-2290
      </li>
      <li>
        <svg viewBox="0 0 24 24" aria-hidden="true"><rect x="2.5" y="5" width="19" height="14" fill="none" stroke="#0c3fa6" stroke-width="2"/><path d="M3 6l9 7 9-7" fill="none" stroke="#0c3fa6" stroke-width="2"/></svg>
        info@corvelladvisory.com
      </li>
      <li>
        <svg viewBox="0 0 24 24" aria-hidden="true"><g fill="none" stroke="#0c3fa6" stroke-width="1.6"><circle cx="12" cy="12" r="9.5"/><ellipse cx="12" cy="12" rx="4" ry="9.5"/><path d="M2.5 12h19M4 7h16M4 17h16"/></g></svg>
        www.corvelladvisory.com
      </li>
    </ul>
  </div>

  <div class="wordmark"><span class="wordmark__dot"></span>Corvell Advisory</div>
  <div class="divider"></div>
  <address class="address">
    Corvell Advisory Ltd<br>
    48 Harbor Lane, Suite 4<br>
    Dunmore, ME 04512
  </address>
</section>

</body>
</html>
```